Business Card Design

The image I attached was a quick thought to my design. I have triplets and was invisioning something with three figures with maybe the colors blue, pink and green. I would like it to look very chic and modern yet soothing/healing. I will take any fresh ideas as well.

Side 1: Contact Details
Side 2: Appointment section (mandatory)
Updates

Thank u all for your preliminary designs. I had sent the old design over and am looking for a bold fresh NEW LOOK  for CORE MOTION. I saw some really creative ideas in the gallery. If you have any other questions please feel free to email me at rtbwakes@quellmail.net.

Thanks

Please keep in mind that it is mandatory that on the back of the card is for appointments.

Thank you.

Reason: The two mandatory elements that need to be on the card is that her title needs to read as so:

Reason: The criteria is still not being met. Her title needs to read as so: Dr. Marisa Kettner, P.T., D.P.T. Doctor of Physical Therapy and The appointment info must go on the BACK of the card. Looking forward to some more great designs. Thanks.

Industry/Entity Type

Business

Contact Information for Business Card

Core Motion
Physical & Aquatic Therapy
Dr. Marisa Kettner, P.T., D.P.T.
Doctor of Physical Therapy

22-48 B Birchwick Lane
Elmbury, N.Y. 11592
(Located inside of the Summit gym in the Pinecrest shopping center)

Phone & Fax: (631) 555-0172
Mkettner4@harbornet.net

Requirements
Must have
• One the back I would like to do an appointment layout.

```html
<!DOCTYPE html>
<html lang="en">
<head>
<meta charset="utf-8">
<title>Core Motion – Business Card</title>
<link rel="stylesheet" href="https://fonts.googleapis.com/css2?family=Montserrat:wght@500;600;700&family=Oswald:wght@300;600&family=Fira+Sans:wght@400;600&family=Source+Serif+4:ital,opsz,wght@1,8..60,400&display=swap">
<style>
  :root {
    --stage: #3b3b3d;
    --blue: #43aee0;
    --green: #abc33e;
    --pink: #d41e69;
    --ink: #0d0d0d;
    --white: #ffffff;
  }
  * { margin: 0; padding: 0; box-sizing: border-box; }
  html, body { width: 1200px; height: 786px; overflow: hidden; background: var(--stage); }
  .canvas { position: relative; width: 1200px; height: 786px; }

  .card { position: absolute; overflow: hidden; background: var(--blue); }
  .card--bold { left: 62px; top: 97px; width: 515px; height: 286px; }
  .card--italic { left: 62px; top: 418px; width: 515px; height: 285px; }
  .card--appointment { left: 624px; top: 418px; width: 514px; height: 287px; }

  .block { position: absolute; }
  .block--green { background: var(--green); }
  .block--pink { background: var(--pink); }

  .line { position: absolute; white-space: nowrap; color: var(--white); }

  /* bold condensed version */
  .card--bold .name { font: 700 20px/1 'Montserrat', sans-serif; left: 9px; top: 33px; }
  .card--bold .detail { font: 500 18.5px/1 'Montserrat', sans-serif; left: 7px; }
  .card--bold .address { font: 300 19px/1 'Oswald', sans-serif; left: 7px; letter-spacing: -0.2px; }
  .card--bold .title {
    position: absolute; right: 12px;
    font-family: 'Oswald', sans-serif; font-weight: 600; color: var(--ink);
    text-transform: uppercase; line-height: 1; white-space: nowrap;
    transform-origin: right top; transform: scaleX(var(--squeeze, 1));
  }

  /* italic serif version */
  .card--italic .name { font: 600 24px/1 'Fira Sans', sans-serif; left: 18px; top: 32px; }
  .card--italic .detail { font: 400 17.5px/1 'Fira Sans', sans-serif; left: 23px; letter-spacing: 0.3px; }
  .card--italic .address { font: 400 16px/1 'Fira Sans', sans-serif; left: 6px; }
  .card--italic .title {
    position: absolute; right: 22px;
    font-family: 'Source Serif 4', serif; font-style: italic; font-weight: 400;
    color: var(--ink); line-height: 1; white-space: nowrap;
  }

  /* appointment back */
  .card--appointment .field { font: 400 18px/1 'Fira Sans', sans-serif; left: 18px; letter-spacing: 0.4px; }
  .card--appointment .heading {
    position: absolute; left: 240px; top: 158px;
    font: 600 53px/1 'Oswald', sans-serif; color: var(--ink);
    transform-origin: left top; transform: scaleX(0.98);
  }
</style>
</head>
<body>
<main class="canvas">

  <!-- Front: bold condensed -->
  <section class="card card--bold">
    <div class="block block--green" style="left:0;top:0;width:236px;height:85px"></div>
    <div class="block block--green" style="left:0;top:85px;width:396px;height:29px"></div>
    <div class="block block--green" style="left:0;top:114px;width:308px;height:29px"></div>
    <div class="block block--green" style="left:0;top:143px;width:281px;height:28px"></div>
    <div class="block block--pink" style="left:0;top:195px;width:192px;height:28px"></div>
    <div class="block block--pink" style="left:0;top:223px;width:170px;height:27px"></div>
    <div class="block block--pink" style="left:0;top:250px;width:515px;height:36px"></div>

    <p class="line name">Dr. Marisa Kettner</p>
    <p class="line detail" style="top:87px">P.T., D.P.T. Doctor of Physical Therapy</p>
    <p class="line detail" style="top:116px">Phone &amp; Fax: (631) 555-0172</p>
    <p class="line detail" style="top:145px">Mkettner4@harbornet.net</p>
    <p class="line address" style="top:196px">22-48 B Birchwick Lane</p>
    <p class="line address" style="top:224px">Elmbury, N.Y. 11592</p>
    <p class="line address" style="top:253px">(Located inside of the Summit gym in the Pinecrest shopping center)</p>

    <h1 class="title" style="top:16px;font-size:54px;--squeeze:0.82">Core Motion</h1>
    <p class="title" style="top:83px;font-size:32px;--squeeze:0.8">Phisical</p>
    <p class="title" style="top:120px;font-size:45px;--squeeze:0.88;right:16px">&amp; Aquatic</p>
    <p class="title" style="top:170px;font-size:84px;--squeeze:0.8">Therapy</p>
  </section>

  <!-- Front: italic serif -->
  <section class="card card--italic">
    <div class="block block--green" style="left:0;top:0;width:248px;height:84px"></div>
    <div class="block block--green" style="left:0;top:84px;width:342px;height:28px"></div>
    <div class="block block--green" style="left:0;top:112px;width:278px;height:29px"></div>
    <div class="block block--green" style="left:0;top:141px;width:234px;height:31px"></div>
    <div class="block block--pink" style="left:0;top:202px;width:221px;height:28px"></div>
    <div class="block block--pink" style="left:0;top:230px;width:225px;height:22px"></div>
    <div class="block block--pink" style="left:0;top:252px;width:515px;height:33px"></div>

    <h2 class="line name">Dr. Marisa Kettner</h2>
    <p class="line detail" style="top:88px">P.T., D.P.T. Doctor of Physical Therapy</p>
    <p class="line detail" style="top:116px">Phone &amp; Fax: (631) 555-0172</p>
    <p class="line detail" style="top:144px">Mkettner4@harbornet.net</p>
    <p class="line address" style="top:209px">22-48 B Birchwick Lane</p>
    <p class="line address" style="top:234px">Elmbury, N.Y. 11592</p>
    <p class="line address" style="top:260px">(Located inside of the Summit gym in the Pinecrest shopping center)</p>

    <p class="title" style="top:26px;font-size:42px">core motion</p>
    <p class="title" style="top:74px;font-size:32px;right:27px">phisical</p>
    <p class="title" style="top:118px;font-size:44px;right:29px">&amp; aquatic</p>
    <p class="title" style="top:160px;font-size:72px;right:31px">therapy</p>
  </section>

  <!-- Back: appointment -->
  <section class="card card--appointment">
    <div class="block block--green" style="left:0;top:0;width:247px;height:84px"></div>
    <div class="block block--green" style="left:0;top:84px;width:341px;height:29px"></div>
    <div class="block block--green" style="left:0;top:113px;width:279px;height:29px"></div>
    <div class="block block--green" style="left:0;top:142px;width:236px;height:31px"></div>
    <div class="block block--pink" style="left:0;top:204px;width:236px;height:28px"></div>
    <div class="block block--pink" style="left:0;top:232px;width:224px;height:20px"></div>
    <div class="block block--pink" style="left:0;top:252px;width:514px;height:35px"></div>

    <p class="line field" style="top:67px">date.................</p>
    <p class="line field" style="top:96px">time.................</p>
    <h2 class="heading">appointment</h2>
  </section>

</main>
</body>
</html>
```